Project Name Card Design, Verdano Cargo

Company Profile
Verdano Cargo Sdn Bhd is a well-established and experienced freight forwarder in Kuala Lumpur, Malaysia. We specialize in air and sea forwarding, Custom Brokerage and regulatory compliance services, inland transportation, overseas freighting and warehousing and distribution management. With our dedicated qualified and experienced professionals, we are fully committed to serving our clients.

Our Mission
Based on the motto “Quick, Reliable and Polite”, Verdano Cargo is dedicated to upholding the following three points corporate philosophy:1. Adhering to the principle that “the customer always comes first”.2. Contributing to the development of the local community.3. Making it our duty to be responsible and sincere.

Our Edge
• One-Stop Logistics Solutions
• Extensive Network Throughout Malaysia
• Highly Qualified and Experienced Pool of Professionals
• Comprehensive IT Solutions
• Innovative and Customer-focused Solutions
• Flexible and Consistent in Managing Exceptions
• Total Supply Chain Visibility

Target Market : We sell the logistics services to all the industry in Malaysia. (One Stop Logistics Solutions)

Business Card Detail : I would like to see the logo on the front with the general info.

Must Haves :
1) Name, Title, Office, Cell, Fax, Email, Address, Website
2) Must have complete company name show as : Verdano Cargo Sdn Bhd
3) Must have company registration no, show as : 8057146-P

Nice to Haves : Modern Design Business Card

Target Market(s)

We sell the logistics services to all the industry in Malaysia. (One Stop Logistics Solutions)

Contact Information for Business Card

I would like to see the logo on the front with the general info.

Colors

Designer to choose colors to be used in the design.

Requirements
Must have
• 1) Name, Title, Office, Cell, Fax, Email, Address, Website
• 2) Must have complete company name show as : Verdano Cargo Sdn Bhd
• 3) Must have company registration no, show as : 8057146-P
Nice to have
• Modern Design Business Card
Should not have
• Nil

```html
<!DOCTYPE html>
<html lang="en">
<head>
<meta charset="utf-8">
<title>Verdano Cargo – Name Card</title>
<link rel="stylesheet" href="https://fonts.googleapis.com/css2?family=Arimo:wght@400;700&display=swap">
<style>
  :root{
    --navy:#0b4e93;
    --sky:#2ba4e2;
    --paper:#ffffff;
    --backdrop:#e9ebef;
    --ink-soft:#dbe8f6;
  }
  *{margin:0;padding:0;box-sizing:border-box}
  html,body{width:1200px;height:800px;overflow:hidden}
  body{
    background:var(--backdrop);
    font-family:"Arimo",Arial,sans-serif;
    display:flex;align-items:center;justify-content:center;gap:40px;
  }
  .card{
    width:540px;height:309px;position:relative;overflow:hidden;
    box-shadow:0 10px 30px rgba(0,0,0,.18);
  }
  /* front */
  .card--front{background:var(--navy);display:flex;align-items:center;justify-content:center}
  .brand{display:flex;align-items:center;gap:14px}
  .brand__dot{width:46px;height:46px;border:3px solid var(--paper);border-radius:50%}
  .brand__rule{width:1px;height:56px;background:var(--paper);opacity:.8}
  .brand__name{
    color:var(--paper);font-weight:700;font-size:30px;letter-spacing:2px;
    text-transform:uppercase;line-height:1;
  }
  .brand__tagline{
    color:var(--paper);font-weight:700;font-size:11px;letter-spacing:3.4px;
    margin-top:12px;
  }
  /* back */
  .card--back{background:var(--paper);display:flex}
  .back__logo{
    width:205px;display:flex;flex-direction:column;align-items:center;justify-content:center;gap:14px;
  }
  .back__logo .brand__dot{width:56px;height:56px;border-color:var(--navy);border-width:4px}
  .back__logo .brand__name{color:var(--navy);font-size:21px;letter-spacing:1.5px;text-align:center;line-height:1.15}
  .back__info{
    flex:1;background:var(--navy);border-left:4px solid var(--sky);
    color:var(--paper);padding:30px 22px 24px 26px;font-size:10.5px;line-height:1.38;
  }
  .person__name{font-weight:700;font-size:17px;line-height:1.05}
  .person__title{font-size:11px;margin-bottom:12px}
  .company__name{font-weight:700;font-style:italic;font-size:11.5px}
  .company__reg{font-weight:700;font-style:italic;font-size:10.5px;margin-bottom:8px}
  .address{margin-bottom:8px}
  .contacts{list-style:none}
  .contacts li{display:flex;align-items:center;gap:7px}
  .contacts svg{width:10px;height:10px;flex:none}
</style>
</head>
<body>

<section class="card card--front">
  <div>
    <div class="brand">
      <span class="brand__dot"></span>
      <span class="brand__rule"></span>
      <span class="brand__name">Verdano Cargo</span>
    </div>
    <p class="brand__tagline">One Stop Logistics Specialist</p>
  </div>
</section>

<section class="card card--back">
  <div class="back__logo">
    <span class="brand__dot"></span>
    <span class="brand__name">Verdano<br>Cargo</span>
  </div>
  <div class="back__info">
    <p class="person__name">Darren Koh</p>
    <p class="person__title">Managing Director</p>
    <p class="company__name">Verdano Cargo Sdn Bhd</p>
    <p class="company__reg">8057146-P</p>
    <p class="address">No. 8B, 2nd Floor,<br>Jalan Seri Pantai 3/KS4<br>Taman Pantai Indah, 41150 Klang<br>Selangor Darul Ehsan, Malaysia</p>
    <ul class="contacts">
      <li><svg viewBox="0 0 10 10"><rect x="2.5" y="0.5" width="5" height="9" rx="1" fill="none" stroke="#fff"/></svg>(+6012) 547 2096</li>
      <li><svg viewBox="0 0 10 10"><path d="M1 4c0-2 2-3 4-3s4 1 4 3H7V3H3v1zM2 5h6l1 4H1z" fill="#fff"/></svg>(+603) 3362 8810 / 8811</li>
      <li><svg viewBox="0 0 10 10"><rect x="2" y="0.5" width="6" height="3" fill="#fff"/><rect x="0.5" y="4" width="9" height="5.5" rx="1" fill="#fff"/></svg>(+603) 3362 8812</li>
      <li><svg viewBox="0 0 10 10"><rect x="0.5" y="2" width="9" height="6" fill="none" stroke="#fff"/><path d="M0.5 2L5 6l4.5-4" fill="none" stroke="#fff"/></svg>darren.koh@verdanocargo.com.my</li>
      <li><svg viewBox="0 0 10 10"><circle cx="5" cy="5" r="4.5" fill="none" stroke="#fff"/><path d="M0.5 5h9M5 0.5c-2.5 3-2.5 6 0 9M5 0.5c2.5 3 2.5 6 0 9" fill="none" stroke="#fff" stroke-width=".7"/></svg>www.verdanocargo.com.my</li>
    </ul>
  </div>
</section>

</body>
</html>
```